Automotive parts Package (box) design

We are developing a new packaging concept for our automotive service and suspension parts line. I will share 2–3 sample designs—some from other brands and some AI‑generated—and we need a designer to create a unified, original design direction based on these references.

We already have an established brand name, KEM, along with a logo. The logo may be updated or redesigned, but the brand name KEM must remain.

- The project includes creating the full packaging design for our product boxes, developing or refining the logo if needed.

-Then, after choosing the design, we will apply the same design to 8 boxes with small customisation for each box to match the product.

- The box die-lines will be provided by us.

Attached are a few sample designs. We need you to develop three or more new designs in a similar style. If you have additional creative concepts beyond these references, you are welcome to include them. The only fixed requirement is that the brand name KEM must remain unchanged in all proposed designs.

Box files such as PNG, PDF (ready-to-print file) and Ai (Editable/ Source file) and fonts with 3D mockup images at the end of the project must be given to us.

Target Market(s)

Car spare parts shops

Industry/Entity Type

Auto Parts

Requirements
Must have
• Our brand name KEM
Nice to have
• Package similar to big auto parts suppliers such as PLW, VARNE

```html
<!DOCTYPE html>
<html lang="en">
<head>
<meta charset="utf-8">
<title>KEM Service Parts Box</title>
<link rel="stylesheet" href="https://fonts.googleapis.com/css2?family=Russo+One&family=Montserrat:wght@500&family=Noto+Sans+JP:wght@700&display=swap">
<style>
  :root {
    --kraft: #c9a47a;
    --kraft-side: #c29c71;
    --kraft-edge: #a8845c;
    --ink: #0b0b0b;
    --band-text: #c9a47a;
    --page: #ffffff;
  }
  * { margin: 0; padding: 0; box-sizing: border-box; }
  html, body { width: 1200px; height: 749px; overflow: hidden; background: var(--page); }
  .canvas { position: relative; width: 1200px; height: 749px; }

  .panel { position: absolute; background: var(--kraft); color: var(--ink); overflow: hidden; }
  .panel--top   { left: 75px;  top: 114px; width: 720px; height: 330px; }
  .panel--front { left: 75px;  top: 445px; width: 720px; height: 190px; }
  .panel--side  { left: 796px; top: 445px; width: 330px; height: 190px; background: var(--kraft-side); }

  .brand { position: absolute; display: flex; flex-direction: column; line-height: 1; }
  .brand__name { font-family: "Russo One", sans-serif; letter-spacing: 2px; }
  .brand__tag { font-family: "Montserrat", sans-serif; font-weight: 500; letter-spacing: 0.4px; margin-top: 3px; white-space: nowrap; }
  .panel--top .brand { left: 36px; top: 28px; }
  .panel--top .brand__name { font-size: 56px; }
  .panel--top .brand__tag { font-size: 9px; }
  .panel--front .brand { left: 22px; top: 22px; }
  .panel--front .brand__name { font-size: 40px; }
  .panel--front .brand__tag { font-size: 7px; }
  .panel--side .brand { left: 0; right: 0; top: 44px; align-items: center; }
  .panel--side .brand__name { font-size: 84px; }
  .panel--side .brand__tag { font-size: 11px; margin-top: 4px; }

  .title { position: absolute; left: 0; right: 0; text-align: center; line-height: 1.1; }
  .title__en { font-family: "Russo One", sans-serif; letter-spacing: 1px; }
  .title__jp { font-family: "Noto Sans JP", sans-serif; font-weight: 700; letter-spacing: 4px; }
  .panel--top .title { top: 120px; }
  .panel--top .title__en { font-size: 40px; }
  .panel--top .title__jp { font-size: 24px; }
  .panel--front .title { top: 74px; }
  .panel--front .title__en { font-size: 30px; }
  .panel--front .title__jp { font-size: 19px; }

  .band {
    position: absolute; left: 0; bottom: 0; width: 100%; height: 40px;
    background: var(--ink); color: var(--band-text);
    display: flex; align-items: center; justify-content: center;
    font-family: "Russo One", sans-serif; font-size: 17px; letter-spacing: 2px;
  }

  .warranty { position: absolute; display: flex; align-items: center; gap: 5px; }
  .warranty__num { font-family: "Russo One", sans-serif; line-height: 1; }
  .warranty__words { display: flex; flex-direction: column; font-family: "Russo One", sans-serif; line-height: 1; }
  .panel--top .warranty { right: 30px; bottom: 56px; }
  .panel--top .warranty__num { font-size: 40px; }
  .panel--top .warranty__words span:first-child { font-size: 15px; }
  .panel--top .warranty__words span:last-child { font-size: 11px; }
  .panel--front .warranty { right: 30px; bottom: 16px; }
  .panel--front .warranty__num { font-size: 36px; }
  .panel--front .warranty__words span:first-child { font-size: 14px; }
  .panel--front .warranty__words span:last-child { font-size: 10px; }
</style>
</head>
<body>
<main class="canvas">
  <section class="panel panel--top">
    <div class="brand">
      <span class="brand__name">KEM</span>
      <span class="brand__tag">AUTOMOTIVE COMPONENTS</span>
    </div>
    <div class="title">
      <div class="title__en">SERVICE PARTS</div>
      <div class="title__jp">サービスパーツ</div>
    </div>
    <div class="warranty">
      <span class="warranty__num">6</span>
      <span class="warranty__words"><span>MONTHS</span><span>WARRANTY</span></span>
    </div>
    <div class="band">KEM AUTOMOTIVE COMPONENTS</div>
  </section>

  <section class="panel panel--front">
    <div class="brand">
      <span class="brand__name">KEM</span>
      <span class="brand__tag">AUTOMOTIVE COMPONENTS</span>
    </div>
    <div class="title">
      <div class="title__en">SERVICE PARTS</div>
      <div class="title__jp">サービスパーツ</div>
    </div>
    <div class="warranty">
      <span class="warranty__num">6</span>
      <span class="warranty__words"><span>MONTHS</span><span>WARRANTY</span></span>
    </div>
  </section>

  <section class="panel panel--side">
    <div class="brand">
      <span class="brand__name">KEM</span>
      <span class="brand__tag">AUTOMOTIVE COMPONENTS</span>
    </div>
  </section>
</main>
</body>
</html>
```